" A empresa busca captar recursos junto a pessoas físicas e jurídicas que precisam investir melhor seu dinheiro com menores taxas de administração e melhores rendimentos "

```html
<!DOCTYPE html>
<html lang="pt-BR">
<head>
<meta charset="utf-8">
<title>Valora Investimentos — Envelope e Papel Timbrado</title>
<link rel="stylesheet" href="https://fonts.googleapis.com/css2?family=Saira:wght@600&family=Roboto:wght@400&display=swap">
<style>
  :root {
    --bg: #e6e6e6;
    --ink: #161616;
    --orange: #f26a1b;
    --paper: #ffffff;
    --muted: #bdbdbd;
  }
  * { box-sizing: border-box; margin: 0; padding: 0; }
  html, body { width: 1200px; height: 1200px; overflow: hidden; }
  body { background: var(--bg); position: relative; font-family: 'Roboto', sans-serif; }

  .envelope {
    position: absolute; left: 110px; top: 260px;
    width: 470px; height: 660px;
    background: var(--ink);
    box-shadow: 0 10px 30px rgba(0,0,0,.18);
  }
  .envelope__flap {
    position: absolute; left: 0; top: 0; width: 100%; height: 46px;
  }
  .envelope__strip {
    position: absolute; left: 0; bottom: 0; width: 100%; height: 10px;
    background: var(--orange);
  }
  .brand {
    position: absolute; display: flex; align-items: center; gap: 10px;
    font-family: 'Saira', sans-serif; font-weight: 600;
    letter-spacing: 1px; white-space: nowrap;
  }
  .brand__mark { width: 14px; height: 14px; background: var(--orange); }
  .envelope .brand { left: 50%; top: 140px; transform: translateX(-50%); color: var(--paper); font-size: 24px; }

  .contact {
    position: absolute; left: 28px; bottom: 40px;
    list-style: none; color: var(--muted); font-size: 11px;
  }
  .contact li { display: flex; align-items: center; gap: 8px; margin-top: 7px; }
  .contact svg { width: 14px; height: 14px; flex: none; }

  .letterhead {
    position: absolute; left: 640px; top: 280px;
    width: 450px; height: 640px;
    background: var(--paper);
    box-shadow: 0 10px 30px rgba(0,0,0,.14);
  }
  .letterhead__strip {
    position: absolute; left: 0; bottom: 0; width: 100%; height: 10px;
    background: var(--orange);
  }
  .letterhead .brand { left: 36px; bottom: 46px; color: var(--ink); font-size: 20px; }
</style>
</head>
<body>
  <section class="envelope" aria-label="Envelope">
    <svg class="envelope__flap" viewBox="0 0 470 46" preserveAspectRatio="none">
      <path d="M0 46 L12 6 Q14 0 22 0 L448 0 Q456 0 458 6 L470 46 Z" fill="#f26a1b"/>
    </svg>
    <div class="brand"><span class="brand__mark"></span>VALORA INVESTIMENTOS</div>
    <ul class="contact">
      <li><svg viewBox="0 0 14 14"><circle cx="7" cy="7" r="7" fill="#f26a1b"/><path d="M4.5 3.5l1.5 0 .6 2-1 .8a5 5 0 0 0 2.1 2.1l.8-1 2 .6 0 1.5c-3.5.3-6.3-2.5-6-6z" fill="#161616"/></svg>(11) 5555-0100</li>
      <li><svg viewBox="0 0 14 14"><circle cx="7" cy="7" r="7" fill="#f26a1b"/><rect x="3.5" y="4.5" width="7" height="5" fill="none" stroke="#161616"/><path d="M3.5 4.5 7 7.3 10.5 4.5" fill="none" stroke="#161616"/></svg>contato@valorainvest.com</li>
      <li><svg viewBox="0 0 14 14"><circle cx="7" cy="7" r="7" fill="#f26a1b"/><circle cx="7" cy="7" r="3.5" fill="none" stroke="#161616"/><path d="M3.5 7h7M7 3.5v7" stroke="#161616"/></svg>www.valorainvest.com</li>
      <li><svg viewBox="0 0 14 14"><circle cx="7" cy="7" r="7" fill="#f26a1b"/><path d="M7 11 4.6 7.4A2.6 2.6 0 1 1 9.4 7.4Z" fill="#161616"/></svg>Rua Exemplo, 100 - Centro<br>São Paulo - SP</li>
    </ul>
    <div class="envelope__strip"></div>
  </section>

  <section class="letterhead" aria-label="Papel timbrado">
    <div class="brand"><span class="brand__mark"></span>VALORA INVESTIMENTOS</div>
    <div class="letterhead__strip"></div>
  </section>
</body>
</html>
```